Tracklight Pro gift box design

We need a box designed for our Tracklight Professional (Quorvel Pro)
Our companies website is Quorvel.com.au and the product page is https://quorvel.com.au/professional/
It has recently been certified to AS3547.1:2023
This Breathalyser is specifically designed for use in workplaces like construction and mining sites due to it's fast alcohol screening (passive with no mouthpiece) mode.
We have uploaded the box stencil pdf. Please use this for the design.
Target Market(s)
Workplaces
Industry/Entity Type
Construction, mining, transport
Font styles to use
Other font styles liked:
- Stick with the logo fonts
Colors
Designer to choose colors to be used in the design.
Requirements
Nice to have
- Colours black, red, and white

```html
<!DOCTYPE html>
<html lang="en">
<head>
<meta charset="utf-8">
<title>Quorvel Professional – Box Design</title>
<link rel="stylesheet" href="https://fonts.googleapis.com/css2?family=Saira+Condensed:wght@500;600;700&family=Saira:wght@400;500;600&display=swap">
<style>
  :root {
    --bg: #f2f2f2;
    --yellow: #f2c91e;
    --yellow-deep: #e3b817;
    --black: #161616;
    --charcoal: #2b2a27;
    --white: #ffffff;
    --red: #c8303c;
    --ink: #1c1c1c;
  }
  * { box-sizing: border-box; margin: 0; padding: 0; }
  html, body { width: 1200px; height: 800px; overflow: hidden; background: var(--bg); }
  body { position: relative; font-family: "Saira", sans-serif; }

  .box-net { position: absolute; left: 415px; top: 30px; width: 370px; height: 740px; display: flex; box-shadow: 0 10px 30px rgba(0,0,0,.12); }

  /* Front panel */
  .front-panel { position: relative; width: 240px; height: 740px; background: var(--yellow); overflow: hidden; }
  .top-band { height: 52px; display: flex; align-items: center; justify-content: center; }
  .brand-lockup { display: flex; flex-direction: column; align-items: flex-end; }
  .brand-name { font-family: "Saira Condensed", sans-serif; font-weight: 700; font-size: 22px; line-height: 1; color: var(--ink); letter-spacing: .5px; }
  .brand-url { font-family: "Saira", sans-serif; font-size: 6.5px; color: var(--ink); border-top: 1px solid var(--ink); padding-top: 1px; width: 100%; text-align: right; }

  .hero-photo { position: absolute; left: 0; top: 52px; width: 240px; height: 470px; }
  .hero-title { position: absolute; top: 78px; left: 0; width: 240px; text-align: center; }
  .product-name { font-family: "Saira Condensed", sans-serif; font-weight: 700; font-size: 32px; line-height: 1; color: var(--yellow); }
  .product-line { font-family: "Saira Condensed", sans-serif; font-weight: 700; font-size: 14px; letter-spacing: 2px; color: var(--yellow); margin-top: 2px; }
  .tagline { font-size: 10px; line-height: 1.45; color: var(--white); margin-top: 10px; }

  .feature { position: absolute; left: 14px; width: 90px; text-align: center; }
  .feature svg { display: block; margin: 0 auto 4px; }
  .feature-title { font-size: 7px; font-weight: 500; color: var(--white); line-height: 1.3; }
  .feature-text { font-size: 5.2px; color: var(--yellow); line-height: 1.45; margin-top: 3px; }
  .feature--tech { top: 250px; }
  .feature--portable { top: 368px; }

  .device-photo { position: absolute; left: 112px; top: 210px; width: 100px; height: 420px; }

  .info-block { position: absolute; left: 11px; width: 92px; }
  .info-title { font-size: 8.5px; font-weight: 500; color: var(--white); }
  .info-text { font-size: 5px; line-height: 1.55; color: #fff7cf; margin-top: 4px; }
  .info-block--one { top: 540px; }
  .info-block--two { top: 622px; }

  .care-icons { position: absolute; left: 11px; top: 696px; display: flex; }
  .care-icons svg { display: block; }

  .cert-badge { position: absolute; left: 173px; top: 612px; }

  /* Side panel */
  .side-panel { position: relative; width: 130px; height: 740px; background: var(--yellow-deep); }
  .side-top { height: 52px; }
  .side-dark { height: 287px; background: var(--black); padding-top: 28px; text-align: center; }
  .side-name { font-family: "Saira Condensed", sans-serif; font-weight: 700; font-size: 18px; line-height: 1; color: var(--yellow); }
  .side-line { font-family: "Saira Condensed", sans-serif; font-weight: 600; font-size: 7.5px; letter-spacing: 1.2px; color: var(--yellow); margin-top: 1px; }
  .side-copy { font-size: 5px; line-height: 1.6; color: #d6d6d6; width: 70px; margin: 18px auto 0; }
  .side-copy + .side-copy { margin-top: 40px; }

  .side-features { padding-top: 16px; }
  .side-feature { text-align: center; height: 80px; }
  .side-feature svg { display: block; margin: 0 auto 3px; }
  .side-feature-title { font-size: 5.8px; line-height: 1.35; color: var(--ink); }

  .spec-table { position: absolute; left: 12px; top: 610px; width: 106px; color: var(--ink); }
  .spec-heading { font-size: 8px; border-bottom: 1px solid var(--ink); padding-bottom: 3px; }
  .spec-row { display: flex; justify-content: space-between; margin-top: 14px; font-size: 6px; }
  .spec-row span { border-bottom: 1px solid var(--ink); padding-bottom: 2px; }
  .spec-row span:first-child { width: 24px; }
  .spec-row span:last-child { width: 62px; }
</style>
</head>
<body>
<main class="box-net">

  <section class="front-panel">
    <header class="top-band">
      <div class="brand-lockup">
        <span class="brand-name">QUORVEL</span>
        <span class="brand-url">quorvel.com.au</span>
      </div>
    </header>

    <svg class="hero-photo" viewBox="0 0 240 470" role="img" aria-label="Photo of a worker holding a beer bottle on a work site">
      <defs>
        <linearGradient id="heroShade" x1="0" y1="0" x2="1" y2="1">
          <stop offset="0" stop-color="#3a3833"/>
          <stop offset=".55" stop-color="#2a2824"/>
          <stop offset="1" stop-color="#4a4535"/>
        </linearGradient>
      </defs>
      <path d="M0 0H240V300C220 360 190 420 130 448C90 460 40 462 0 464Z" fill="url(#heroShade)"/>
    </svg>

    <div class="hero-title">
      <div class="product-name">QUORVEL</div>
      <div class="product-line">PROFESSIONAL</div>
      <p class="tagline">Keep Your Workplace<br>Safe &amp; Alcohol-Free</p>
    </div>

    <div class="feature feature--tech">
      <svg width="28" height="28" viewBox="0 0 28 28" aria-hidden="true">
        <circle cx="14" cy="14" r="12.5" fill="none" stroke="#f2c91e" stroke-width="1"/>
        <circle cx="14" cy="14" r="7" fill="none" stroke="#f2c91e" stroke-width="1"/>
        <path d="M14 9.5l1.3 2.8 3 .3-2.3 2 .7 3-2.7-1.6-2.7 1.6.7-3-2.3-2 3-.3z" fill="#f2c91e"/>
      </svg>
      <div class="feature-title">Superior Technology</div>
      <p class="feature-text">Powered by cutting-edge fuel-cell technology, Quorvel is at the forefront of breathalyser innovation</p>
    </div>

    <div class="feature feature--portable">
      <svg width="28" height="36" viewBox="0 0 28 36" aria-hidden="true">
        <ellipse cx="14" cy="18" rx="12.5" ry="16.5" fill="none" stroke="#f2c91e" stroke-width="1"/>
        <rect x="10.5" y="8" width="7" height="20" rx="2" fill="none" stroke="#f2c91e" stroke-width="1"/>
        <rect x="12" y="10.5" width="4" height="5" fill="#f2c91e"/>
        <circle cx="14" cy="22" r="1.6" fill="none" stroke="#f2c91e" stroke-width=".8"/>
      </svg>
      <div class="feature-title">Sleek Portable<br>Design</div>
      <p class="feature-text">Safely store your Quorvel in your glove box or bag so you can test yourself whenever you need to</p>
    </div>

    <svg class="device-photo" viewBox="0 0 100 420" role="img" aria-label="Product photo of the handheld breathalyser">
      <defs>
        <linearGradient id="productTone" x1="0" y1="0" x2="0" y2="1">
          <stop offset="0" stop-color="#3a3833"/>
          <stop offset="1" stop-color="#e2b918"/>
        </linearGradient>
      </defs>
      <rect x="0" y="0" width="100" height="420" fill="url(#productTone)"/>
    </svg>

    <div class="info-block info-block--one">
      <div class="info-title">Lorem ipsum</div>
      <p class="info-text">Lorem ipsum dolor sit amet, consectetuer adipiscing elit, sed diam nonummy nibh euismod tincidunt ut laoreet dolore magna</p>
    </div>
    <div class="info-block info-block--two">
      <div class="info-title">Lorem ipsum</div>
      <p class="info-text">Lorem ipsum dolor sit amet, consectetuer adipiscing elit, sed diam nonummy nibh</p>
    </div>

    <div class="care-icons" aria-hidden="true">
      <svg width="50" height="22" viewBox="0 0 50 22">
        <g fill="none" stroke="#1c1c1c" stroke-width=".9">
          <rect x=".5" y=".5" width="49" height="21"/>
          <line x1="17" y1=".5" x2="17" y2="21.5"/><line x1="33" y1=".5" x2="33" y2="21.5"/>
          <circle cx="8.7" cy="11" r="5"/><rect x="21" y="5" width="8" height="12"/>
          <path d="M41.5 5l5 6-5 6-5-6z"/>
        </g>
        <circle cx="8.7" cy="11" r="2" fill="#1c1c1c"/><rect x="23.5" y="8.5" width="3" height="5" fill="#1c1c1c"/><circle cx="41.5" cy="11" r="1.6" fill="#1c1c1c"/>
      </svg>
    </div>

    <svg class="cert-badge" width="56" height="128" viewBox="0 0 56 128" role="img" aria-label="Certification mark">
      <rect x="0" y="0" width="56" height="128" fill="#ffffff"/>
      <rect x="2" y="2" width="52" height="100" fill="#c8303c"/>
    </svg>
  </section>

  <section class="side-panel">
    <div class="side-top"></div>
    <div class="side-dark">
      <div class="side-name">QUORVEL</div>
      <div class="side-line">PROFESSIONAL</div>
      <p class="side-copy">Fast passive screening for busy sites. No mouthpiece needed, results in seconds for every worker on shift.</p>
      <p class="side-copy">Fuel-cell sensor built for construction, mining and transport crews. Certified to the Australian standard for reliable daily use.</p>
    </div>

    <div class="side-features">
      <div class="side-feature">
        <svg width="22" height="36" viewBox="0 0 22 36" aria-hidden="true"><ellipse cx="11" cy="18" rx="10" ry="16.5" fill="none" stroke="#1c1c1c" stroke-width=".9"/><rect x="8" y="9" width="6" height="18" rx="1.5" fill="none" stroke="#1c1c1c" stroke-width=".9"/><rect x="9.5" y="11.5" width="3" height="4" fill="#1c1c1c"/></svg>
        <div class="side-feature-title">Sleek Portable<br>Design</div>
      </div>
      <div class="side-feature">
        <svg width="22" height="36" viewBox="0 0 22 36" aria-hidden="true"><ellipse cx="11" cy="18" rx="10" ry="16.5" fill="none" stroke="#1c1c1c" stroke-width=".9"/><rect x="8" y="9" width="6" height="18" rx="1.5" fill="none" stroke="#1c1c1c" stroke-width=".9"/><rect x="9.5" y="11.5" width="3" height="4" fill="#1c1c1c"/></svg>
        <div class="side-feature-title">Sleek Portable<br>Design</div>
      </div>
      <div class="side-feature">
        <svg width="22" height="36" viewBox="0 0 22 36" aria-hidden="true"><ellipse cx="11" cy="18" rx="10" ry="16.5" fill="none" stroke="#1c1c1c" stroke-width=".9"/><rect x="8" y="9" width="6" height="18" rx="1.5" fill="none" stroke="#1c1c1c" stroke-width=".9"/><rect x="9.5" y="11.5" width="3" height="4" fill="#1c1c1c"/></svg>
        <div class="side-feature-title">Sleek Portable<br>Design</div>
      </div>
    </div>

    <div class="spec-table">
      <div class="spec-heading">Lorem ipsum</div>
      <div class="spec-row"><span>Lorem</span><span>Lorem ipsum</span></div>
      <div class="spec-row"><span>Lorem</span><span>Lorem ipsum</span></div>
      <div class="spec-row"><span>Lorem</span><span>Lorem ipsum</span></div>
    </div>
  </section>

</main>
</body>
</html>
```